MOLVT Study flyer

I need help designing a flyer for a research study that will include brain imaging in adolescents. The info is in the attached document. The study is called the Marrowby Orchard Lantern Vesper Trail (MOLVT) study. Ideally this would be returned as a document that I can edit in the future as we will have several new recruitment phases (different age groups, etc. I also would love to have a logo designed as part of this project, but I recognize that might be a separate design request.

```html
<!DOCTYPE html>
<html lang="en">
<head>
<meta charset="utf-8">
<title>MOLVT Study Flyer</title>
<link href="https://fonts.googleapis.com/css2?family=Poppins:wght@400;500;600;700;800&display=swap" rel="stylesheet">
<style>
  :root {
    --navy: #103c5e;
    --ink: #1a1a1a;
    --band-blue: #1b5e86;
    --band-teal: #1a7d77;
    --white: #ffffff;
    --purple: #6a3c9e;
    --green: #2f6a2b;
    --gold: #f6c21c;
  }
  * { box-sizing: border-box; margin: 0; padding: 0; }
  html, body { width: 930px; height: 1200px; overflow: hidden; background: var(--white); }
  body { font-family: "Poppins", sans-serif; color: var(--ink); }

  .flyer { position: relative; width: 930px; height: 1200px; overflow: hidden; }

  .masthead { position: absolute; left: 0; top: 0; width: 930px; height: 382px; background: var(--white); }
  .brand { position: absolute; left: 74px; top: 180px; width: 360px; }
  .brand-name {
    font-weight: 700; font-size: 90px; line-height: 1; letter-spacing: 1px; color: var(--navy);
  }
  .brand-tagline {
    margin-top: 12px; font-weight: 500; font-size: 23px; line-height: 1.3; color: var(--ink);
  }
  .hero-visual {
    position: absolute; left: 420px; top: 0; width: 510px; height: 382px;
    background:
      radial-gradient(ellipse at 78% 55%, rgba(245,90,140,0.55), rgba(245,90,140,0) 55%),
      radial-gradient(ellipse at 88% 30%, rgba(250,210,60,0.55), rgba(250,210,60,0) 50%),
      radial-gradient(ellipse at 70% 80%, rgba(120,90,220,0.45), rgba(120,90,220,0) 50%),
      linear-gradient(90deg, #f7f7f7 0%, #e9e9ec 45%, #d9e8f2 100%);
  }

  .intro-band {
    position: absolute; left: 0; top: 382px; width: 930px; height: 224px;
    background: var(--band-blue); color: var(--white); padding: 28px 54px 0;
  }
  .intro-question { font-weight: 700; font-size: 21px; line-height: 1.5; }
  .intro-text { margin-top: 12px; font-weight: 600; font-size: 18.5px; line-height: 1.6; }

  .details {
    position: absolute; left: 0; top: 606px; width: 930px; height: 328px;
    display: flex; padding: 42px 54px 0 62px;
  }
  .details-col.involves { width: 484px; padding-right: 20px; }
  .details-col.eligible { width: 330px; }
  .details-heading { font-weight: 700; font-size: 16px; letter-spacing: 0.2px; text-transform: uppercase; margin-bottom: 12px; }
  .involves .details-heading { color: var(--purple); }
  .eligible .details-heading { color: var(--green); }
  .details-list { list-style: none; }
  .details-list li {
    position: relative; padding-left: 26px; font-size: 18px; line-height: 1.65; font-weight: 500;
  }
  .details-list li::before {
    content: ""; position: absolute; left: 4px; top: 12px; width: 7px; height: 7px;
    border-radius: 50%; background: var(--ink);
  }

  .contact-band {
    position: absolute; left: 0; top: 934px; width: 930px; height: 266px;
    background: var(--band-teal); color: var(--white); padding: 38px 54px 0;
  }
  .contact-heading { font-weight: 700; font-size: 21px; }
  .contact-lines { margin-top: 6px; font-weight: 500; font-size: 18px; line-height: 1.82; }

  .compensation {
    position: absolute; left: 464px; top: 154px; width: 410px; height: 60px;
    border: 2px dashed var(--white); display: flex; align-items: center; justify-content: center;
    color: var(--white); font-weight: 700; font-size: 22px; letter-spacing: 0.6px;
  }
  .compensation .amount { color: var(--gold); margin-left: 8px; }
</style>
</head>
<body>
  <main class="flyer">
    <header class="masthead">
      <div class="brand">
        <div class="brand-name">MOLVT</div>
        <p class="brand-tagline">Marrowby Orchard Lantern<br>Vesper Trail</p>
      </div>
      <div class="hero-visual" role="img" aria-label="Photo of a thoughtful teenage girl in front of a brain illustration with maths scribbles on one side and colourful paint splashes on the other"></div>
    </header>

    <section class="intro-band">
      <h1 class="intro-question">Are you the parent of a child age 10–17? Do they worry overthink negative emotions?</h1>
      <p class="intro-text">Harrowgate University researchers are seeking girls age 10-17 for a study about brain activity in emotions and decision-making and how they relate to puberty, anxiety and depression.</p>
    </section>

    <section class="details">
      <div class="details-col involves">
        <h2 class="details-heading">Study participation involves:</h2>
        <ul class="details-list">
          <li>One one-hour interview (online or in-person) where your child will discuss their thoughts</li>
          <li>Online questionnaires (parent and child)</li>
          <li>One two-hour visit where your child will complete an MRI scan, answer questions about their puberty stage, and have a small hair sample taken to study puberty hormones</li>
        </ul>
      </div>
      <div class="details-col eligible">
        <h2 class="details-heading">Your child may be eligible if they:</h2>
        <ul class="details-list">
          <li>Are age 10-17</li>
          <li>Tend to worry or overthink negative thoughts</li>
          <li>Have not been diagnosed with psychosis, learning problems, or autism</li>
        </ul>
      </div>
    </section>

    <footer class="contact-band">
      <h2 class="contact-heading">Interested in participating? Want more information? Please contact us!</h2>
      <p class="contact-lines">Phone: 412-555-0187<br>Email: molvt@harrowgate.edu<br>Website: harrowgate.edu/molvt</p>
      <div class="compensation">COMPENSATION UP TO <span class="amount">$140</span></div>
    </footer>
  </main>
</body>
</html>
```